Lead Sales Portal Needs to Generate B2B Signup's

We are looking for banner ad designs to drive new business (B2B) traffic to our insurance and mortgage industry self serve lead sites. The sites are HomeLoanProspectHub.com and PolicyProspectHub.com, and we service over 45,000 insurance agents and mortgage lenders in a self serve lead portal model. We want our banners to generate more of these clients.

Our clients come to our sites, browse our database and then pick out and purchase the consumer leads that they need to generate new business.

We advertise extensively on Zorvia and on other PPC platforms, and our existing banners are looking really tired.

Some of the ad copy that works well for us is:

Cherry Pick Your Life Leads - Why Pay More Than $3.50 For Life Insurance Leads?
Sign up today and we'll match up to $250

Agents - Here's $250 For New Clients. Cherry Pick Your Life Insurance Leads & Save! Sign up today and we'll match up to $250

One of our Landing Pages that performs well is here:
http://www.policyprospecthub.com/lp/008/

One of our competitors ad's are here:

http://www.adwatchery.com/search/results?q=RateBeacon&ad=518294

We're looking for a design that is eye catching, uses our "Deeply Discounted Leads" and our "$250 match bonus"

Target Market(s)

These are insurance agents and mortgage lenders. All of our clients are business' or individuals within the business. This is a B2B campaign,

Industry/Entity Type

Insurance

Requirements
Must have
• We must have the logos for the sites in the banners. Also, we must have a call to action arrow and "Go" button

One or two designs.

File type

.JPEG
.JPG
.PNG
.GIF

File size

150 KB or smaller

Image sizes

Vertical rectangle: 240 x 400
Mobile leaderboard: 320 x 50
Banner: 468 x 60
Leaderboard: 728 x 90
Square: 250 x 250
Small square: 200 x 200
Large rectangle: 336 x 280
Inline rectangle: 300 x 250
Skyscraper: 120 x 600
Wide skyscraper: 160 x 600
Half-page: 300 x 600
Large leaderboard: 970 x 90

```html
<!DOCTYPE html>
<html lang="en">
<head>
<meta charset="utf-8">
<title>Policy Prospect Hub – Banner Set</title>
<link href="https://fonts.googleapis.com/css2?family=Oswald:wght@500&family=Roboto+Condensed:wght@400;700&display=swap" rel="stylesheet">
<style>
  :root{
    --stage:#ececec;
    --panel-top:#2e2e2e;
    --panel-bottom:#1b1b1b;
    --yellow:#ffcc00;
    --yellow-deep:#f5a800;
    --white:#ffffff;
    --ink:#1a1a1a;
    --silver:#c9c9c9;
    --photo-a:#d9dde2;
    --photo-b:#3a3d44;
  }
  *{margin:0;padding:0;box-sizing:border-box}
  html,body{width:1200px;height:649px;overflow:hidden;background:var(--stage)}
  .canvas{position:relative;width:1200px;height:649px}
  .banner{position:absolute;overflow:hidden;background:linear-gradient(180deg,var(--panel-top),var(--panel-bottom));
    box-shadow:0 2px 8px rgba(0,0,0,.25);font-family:"Roboto Condensed",sans-serif;color:var(--white)}
  .photo{position:absolute;background:linear-gradient(160deg,var(--photo-a) 0%,#b9bcc2 45%,var(--photo-b) 100%)}
  .head{position:absolute;font-family:"Oswald",sans-serif;font-weight:500;text-transform:uppercase;line-height:1.05;letter-spacing:-.2px;text-align:center;white-space:nowrap}
  .yellow{color:var(--yellow)}
  .bullets{position:absolute;list-style:none;white-space:nowrap}
  .bullets li{position:relative;padding-left:1.15em;line-height:1.3}
  .bullets.tight li{line-height:1.2}
  .bullets li::before{content:"";position:absolute;left:.2em;top:.12em;width:.36em;height:.7em;
    border-right:.17em solid var(--yellow);border-bottom:.17em solid var(--yellow);transform:rotate(40deg)}
  .footer{position:absolute;background:var(--white);z-index:1}
  .logo{position:absolute;z-index:2;display:flex;align-items:center;gap:.3em;color:var(--ink);font-family:"Roboto Condensed",sans-serif;font-weight:400;white-space:nowrap}
  .logo .mark{width:1.5em;height:1.5em;border-radius:50%;background:var(--ink);flex:none}
  .go{position:absolute;z-index:3;display:flex;align-items:center;justify-content:center;gap:.35em;border-radius:3px;
    background:linear-gradient(180deg,#ffe04d,var(--yellow) 50%,var(--yellow-deep));color:var(--ink);
    font-family:"Oswald",sans-serif;font-weight:500;box-shadow:0 1px 2px rgba(0,0,0,.4)}
  .go svg{width:1em;height:1em}
  .rule{position:absolute;height:1px;background:linear-gradient(90deg,transparent,#777,transparent)}
  .chevron-band{position:absolute}
</style>
</head>
<body>
<div class="canvas">

  <!-- Half page 300x600 -->
  <section class="banner half-page" style="left:48px;top:74px;width:265px;height:530px">
    <div class="photo" role="img" aria-label="Photo of two smiling business professionals in dark suits" style="left:0;top:0;width:265px;height:262px"></div>
    <svg class="chevron-band" style="left:0;top:240px" width="265" height="30" viewBox="0 0 265 30" aria-hidden="true">
      <polygon points="0,22 132,4 265,22 265,30 0,30" fill="var(--silver)"/>
      <polygon points="0,28 132,10 265,28 265,30 0,30" fill="var(--panel-top)"/>
    </svg>
    <div class="head" style="left:0;width:265px;top:276px;font-size:22px;line-height:1.2">
      Pick your life<br><span class="yellow">Insurance leads &amp; save!</span>
    </div>
    <div class="rule" style="left:25px;width:215px;top:335px"></div>
    <div class="head" style="left:0;width:265px;top:343px;font-size:19px">We'll match</div>
    <div class="head yellow" style="left:0;width:265px;top:366px;font-size:33px">Up to $250</div>
    <ul class="bullets" style="left:48px;top:413px;font-size:15px">
      <li>Starting at $3.50 / lead</li><li>No Minimums .</li><li>Deeply discounted leads.</li>
    </ul>
    <div class="footer" style="left:0;top:482px;width:265px;height:48px"></div>
    <div class="logo" style="left:8px;top:494px;font-size:16px"><span class="mark"></span>Policy Prospect Hub</div>
    <div class="go" style="left:189px;top:491px;width:63px;height:29px;font-size:17px">GO
      <svg viewBox="0 0 20 20" aria-hidden="true"><circle cx="10" cy="10" r="10" fill="#333"/><path d="M8 5l5 5-5 5" stroke="#fff" stroke-width="2.4" fill="none"/></svg></div>
  </section>

  <!-- Wide skyscraper 160x600 -->
  <section class="banner skyscraper" style="left:338px;top:74px;width:141px;height:530px">
    <div class="photo" role="img" aria-label="Photo of two smiling business professionals in dark suits" style="left:0;top:0;width:141px;height:232px"></div>
    <svg class="chevron-band" style="left:0;top:214px" width="141" height="26" viewBox="0 0 141 26" aria-hidden="true">
      <polygon points="0,20 70,4 141,20 141,26 0,26" fill="var(--silver)"/>
      <polygon points="0,25 70,9 141,25 141,26 0,26" fill="var(--panel-top)"/>
    </svg>
    <div class="head" style="left:0;width:141px;top:246px;font-size:19px;line-height:1.12">
      Pick your life<br><span class="yellow" style="font-size:26px">Insurance</span><br>Leads &amp; save!
    </div>
    <div class="head" style="left:0;width:141px;top:344px;font-size:15px">We'll match</div>
    <div class="head yellow" style="left:0;width:141px;top:362px;font-size:25px">Up to $250</div>
    <ul class="bullets" style="left:5px;top:399px;font-size:11.5px">
      <li>Starting at $3.50 / lead</li><li>No Minimums .</li><li>Deeply discounted leads.</li>
    </ul>
    <div class="footer" style="left:0;top:473px;width:141px;height:57px"></div>
    <div class="go" style="left:38px;top:456px;width:63px;height:28px;font-size:16px">GO
      <svg viewBox="0 0 20 20" aria-hidden="true"><circle cx="10" cy="10" r="10" fill="#333"/><path d="M8 5l5 5-5 5" stroke="#fff" stroke-width="2.4" fill="none"/></svg></div>
    <div class="logo" style="left:7px;top:497px;font-size:13px"><span class="mark"></span>Policy Prospect Hub</div>
  </section>

  <!-- Large rectangle 336x280 -->
  <section class="banner large-rectangle" style="left:523px;top:116px;width:296px;height:247px">
    <div class="photo" role="img" aria-label="Photo of two smiling business professionals in dark suits" style="left:138px;top:0;width:158px;height:247px;clip-path:polygon(8px 0,100% 0,100% 100%,8px 100%,22px 50%)"></div>
    <div class="head" style="left:0;width:144px;top:10px;font-size:20px">
      Pick your life<br><span class="yellow" style="font-size:25px">Insurance</span><br>Leads &amp; save!
    </div>
    <div class="head" style="left:0;width:144px;top:97px;font-size:15px">We'll match</div>
    <div class="head yellow" style="left:0;width:144px;top:114px;font-size:25px">Up to $250</div>
    <ul class="bullets" style="left:4px;top:153px;font-size:11.5px">
      <li>Starting at $3.50 / lead</li><li>No Minimums .</li><li>Deeply discounted leads.</li>
    </ul>
    <div class="go" style="left:34px;top:209px;width:63px;height:27px;font-size:16px">GO
      <svg viewBox="0 0 20 20" aria-hidden="true"><circle cx="10" cy="10" r="10" fill="#333"/><path d="M8 5l5 5-5 5" stroke="#fff" stroke-width="2.4" fill="none"/></svg></div>
    <div class="footer" style="left:145px;top:208px;width:151px;height:39px"></div>
    <div class="logo" style="left:152px;top:218px;font-size:14px"><span class="mark"></span>Policy Prospect Hub</div>
  </section>

  <!-- Inline rectangle 300x250 -->
  <section class="banner inline-rectangle" style="left:844px;top:143px;width:265px;height:220px">
    <div class="photo" role="img" aria-label="Photo of two smiling business professionals in dark suits" style="left:120px;top:0;width:145px;height:220px;clip-path:polygon(6px 0,100% 0,100% 100%,6px 100%,18px 50%)"></div>
    <div class="head" style="left:0;width:126px;top:8px;font-size:18px">
      Pick your life<br><span class="yellow" style="font-size:23px">Insurance</span><br>Leads &amp; save!
    </div>
    <div class="head" style="left:0;width:126px;top:87px;font-size:14px">We'll match</div>
    <div class="head yellow" style="left:0;width:126px;top:103px;font-size:23px">Up to $250</div>
    <ul class="bullets tight" style="left:2px;top:138px;font-size:10.5px">
      <li>Starting at $3.50 / lead</li><li>No Minimums .</li><li>Deeply discounted leads.</li>
    </ul>
    <div class="go" style="left:31px;top:186px;width:56px;height:24px;font-size:14px">GO
      <svg viewBox="0 0 20 20" aria-hidden="true"><circle cx="10" cy="10" r="10" fill="#333"/><path d="M8 5l5 5-5 5" stroke="#fff" stroke-width="2.4" fill="none"/></svg></div>
    <div class="footer" style="left:125px;top:185px;width:140px;height:35px"></div>
    <div class="logo" style="left:130px;top:194px;font-size:13px"><span class="mark"></span>Policy Prospect Hub</div>
  </section>

  <!-- Banner 468x60 -->
  <section class="banner banner-468" style="left:523px;top:404px;width:413px;height:51px">
    <div class="photo" role="img" aria-label="Photo of two smiling business professionals" style="left:0;top:0;width:128px;height:51px;clip-path:polygon(0 0,118px 0,128px 50%,118px 100%,0 100%)"></div>
    <div class="head" style="left:124px;top:3px;font-size:11px;width:78px">
      Pick your life<br><span class="yellow" style="font-size:15px">Insurance</span><br>Leads &amp; save!
    </div>
    <div class="head" style="left:214px;top:4px;font-size:9.5px;text-align:left">We'll match <span class="yellow">up to $250</span></div>
    <ul class="bullets tight" style="left:210px;top:17px;font-size:7.5px">
      <li>Starting at $3.50 / lead</li><li>No Minimums .</li><li>Deeply discounted leads.</li>
    </ul>
    <div class="footer" style="left:318px;top:0;width:95px;height:51px"></div>
    <div class="go" style="left:347px;top:6px;width:42px;height:18px;font-size:11px">GO
      <svg viewBox="0 0 20 20" aria-hidden="true"><circle cx="10" cy="10" r="10" fill="#333"/><path d="M8 5l5 5-5 5" stroke="#fff" stroke-width="2.4" fill="none"/></svg></div>
    <div class="logo" style="left:322px;top:31px;font-size:9px"><span class="mark"></span>Policy Prospect Hub</div>
  </section>

  <!-- Leaderboard 728x90 -->
  <section class="banner leaderboard" style="left:523px;top:476px;width:642px;height:79px">
    <div class="photo" role="img" aria-label="Photo of two smiling business professionals" style="left:0;top:0;width:185px;height:79px;clip-path:polygon(0 0,170px 0,185px 50%,170px 100%,0 100%)"></div>
    <div class="head" style="left:190px;top:3px;font-size:18px;width:125px">
      Pick your life<br><span class="yellow" style="font-size:24px">Insurance</span><br>Leads &amp; save!
    </div>
    <div class="head" style="left:332px;top:7px;font-size:14.5px;text-align:left">We'll match <span class="yellow">up to $250</span></div>
    <ul class="bullets" style="left:330px;top:30px;font-size:12px">
      <li>Starting at $3.50 / lead</li><li>No Minimums .</li><li>Deeply discounted leads.</li>
    </ul>
    <div class="footer" style="left:495px;top:0;width:147px;height:79px"></div>
    <div class="go" style="left:537px;top:12px;width:63px;height:28px;font-size:16px">GO
      <svg viewBox="0 0 20 20" aria-hidden="true"><circle cx="10" cy="10" r="10" fill="#333"/><path d="M8 5l5 5-5 5" stroke="#fff" stroke-width="2.4" fill="none"/></svg></div>
    <div class="logo" style="left:504px;top:52px;font-size:13px"><span class="mark"></span>Policy Prospect Hub</div>
  </section>

</div>
</body>
</html>
```